Business Card Design

Hello Designer,
This is an internet based company. We specialize in low rate advertisement space on a number of our websites, Similar to roamjournal. We also Do keyword seo, social media development and management, website development,and mobile friendly reformatting of websites. The overall design should communicate Brightlane Links provides customers with easy access to our advertised businesses, to connect businesses to their desired customers and vice versa.
Updates

Hello Designers!,

If you would like to view my website for ideas please visit. sarasotaventro.example
Also I would like the "BRIGHTLANE LINKS" lettering to be different colors, like Zentros lettering. Also the color scheme I was thinking was blue, white, black
Thank you for taking on this project,
CorinĀ 

Industry/Entity Type

Internet

Contact Information for Business Card

Brightlane Links,Corin Mossfeld,CEO, corin@ventrowww.example, CELL: 941-555-0162, 4182 Larkspur Ln Sarasota 34231,corin@ventrowww.example, Making The Internet More Affordable and Manageable,sarasotaventro.example
ON BACK: Making The Internet More Affordable and Manageable, sarasotaventro,tampaventro,miamiventro,pensacolaventro,jacksonvilleventro, and more, many more.

```html
<!DOCTYPE html>
<html lang="en">
<head>
<meta charset="utf-8">
<title>Brightlane Links – Business Card</title>
<link rel="stylesheet" href="https://fonts.googleapis.com/css2?family=Michroma&family=Exo+2:wght@400;500;600&display=swap">
<style>
  :root {
    --brand-blue: #3d3d98;
    --ink: #2b2b2b;
    --rule-dark: #3a3a3a;
    --paper-light: #ffffff;
    --paper-shade: #e4e4e6;
    --backdrop: #d9d9dc;
    --band-text: #ffffff;
  }
  * { box-sizing: border-box; margin: 0; padding: 0; }
  html, body { width: 1200px; height: 903px; overflow: hidden; }
  body { background: var(--backdrop); position: relative; font-family: "Exo 2", sans-serif; }

  .card {
    position: absolute;
    width: 640px;
    height: 366px;
    background: radial-gradient(ellipse at 60% 45%, var(--paper-light) 0%, #f4f4f5 45%, var(--paper-shade) 100%);
    box-shadow: 0 10px 24px rgba(0,0,0,0.25);
    overflow: hidden;
  }
  .card--back { left: 90px; top: 60px; }
  .card--front { left: 470px; top: 470px; }

  .brand-name {
    font-family: "Michroma", sans-serif;
    font-variant: small-caps;
    color: var(--brand-blue);
    letter-spacing: 3px;
    white-space: nowrap;
  }

  /* Back */
  .card--back .brand-name { position: absolute; left: 46px; top: 140px; font-size: 27px; }
  .social-band {
    position: absolute; left: 0; right: 0; top: 196px; height: 78px;
    background: var(--brand-blue);
    display: flex; align-items: center; justify-content: flex-end;
    padding-right: 30px; gap: 14px;
    color: var(--band-text);
  }
  .social-band__lead { font-size: 22px; letter-spacing: 1px; margin-right: 6px; }
  .social-name { font-size: 14px; font-weight: 600; display: flex; align-items: center; gap: 5px; }
  .social-name::before { content: ""; width: 8px; height: 8px; border-radius: 50%; background: var(--band-text); }

  /* Front */
  .person { position: absolute; left: 40px; top: 34px; }
  .person__name { font-size: 29px; font-weight: 500; color: var(--brand-blue); letter-spacing: 1px; }
  .person__role { font-size: 16px; font-weight: 500; color: var(--ink); letter-spacing: 1px; margin-top: 2px; }

  .contact-list { position: absolute; left: 24px; top: 118px; width: 340px; }
  .contact-rule { height: 2px; background: var(--brand-blue); }
  .contact-rule--dark { background: var(--rule-dark); }
  .contact-row { display: flex; align-items: center; gap: 14px; padding: 10px 0 10px 14px; }
  .contact-row svg { flex: none; }
  .contact-text { font-size: 15px; line-height: 1.5; color: var(--ink); letter-spacing: 0.8px; white-space: nowrap; }

  .card--front .brand-name {
    position: absolute; left: 398px; top: 176px;
    font-size: 25px; line-height: 1.6; letter-spacing: 2px;
  }
</style>
</head>
<body>

<section class="card card--back" aria-label="Card back">
  <div class="brand-name">Brightlane Links</div>
  <div class="social-band">
    <span class="social-band__lead">follow us on here:</span>
    <span class="social-name">Chirpa</span>
    <span class="social-name">Frendo</span>
    <span class="social-name">Blogli</span>
    <span class="social-name">Vidora</span>
  </div>
</section>

<section class="card card--front" aria-label="Card front">
  <div class="person">
    <div class="person__name">CORIN MOSSFELD</div>
    <div class="person__role">CEO</div>
  </div>

  <div class="contact-list">
    <div class="contact-rule"></div>
    <div class="contact-row">
      <svg width="16" height="22" viewBox="0 0 16 22" aria-hidden="true">
        <path d="M4 1 L7 1 L8 6 L6 8 C6 12 8 15 10 16 L12 14 L15 16 L14 20 C8 21 1 13 2 4 Z" fill="var(--brand-blue)"/>
      </svg>
      <div class="contact-text">CELL: 941-555-0162</div>
    </div>
    <div class="contact-rule contact-rule--dark"></div>
    <div class="contact-row">
      <svg width="16" height="22" viewBox="0 0 16 22" aria-hidden="true">
        <path d="M8 1 C3.5 1 1 4.5 1 8 C1 13 8 21 8 21 C8 21 15 13 15 8 C15 4.5 12.5 1 8 1 Z M8 5 A3 3 0 1 1 8 11 A3 3 0 1 1 8 5 Z" fill="var(--brand-blue)" fill-rule="evenodd"/>
      </svg>
      <div class="contact-text">4182 Larkspur Ln Sarasota 34231</div>
    </div>
    <div class="contact-rule"></div>
    <div class="contact-row">
      <svg width="20" height="18" viewBox="0 0 20 18" aria-hidden="true">
        <rect x="1" y="1" width="18" height="12" fill="none" stroke="var(--brand-blue)" stroke-width="1.6"/>
        <path d="M7 17 H13 M10 13 V17" stroke="var(--brand-blue)" stroke-width="1.6"/>
      </svg>
      <div class="contact-text">corin@ventrowww.example<br>sarasotaventro.example</div>
    </div>
    <div class="contact-rule"></div>
  </div>

  <div class="brand-name">Brightlane<br>Links</div>
</section>

</body>
</html>
```